Grain Roll Package Re-Design (Food)

Attached is our current package design. We need complete re-design of our current package. Here are changes needed:

1) Product name:
Product name doesn't catch consumer's eyes. Product name itself must stand out. By looking at the product name, consumer must get an idea of what this product is.
Also, product name needs to be changed to 'Oven Puffed Harvest Crunch Rounds'.

Also the main feature of this product is that it is made of 21 Multi Grains. So this must be reflected clearly on the package! Without reading the package, consumer must clearly understand that this product is made of 21 Multi Grains therefore, it is a healthy snack, great replacement for meals.

2) Product actual size picture:
On the front side of the package, there must be an actual size of the product.

3) Net Weight
Needs to be 2.82 oz (80g)

4) Pelno logo needs to be changed to the new uploaded one (with grandma face).

5) Dovalin, Inc logo attached (Manufactured exclusively for Dovalin, Inc.)

6) Example package we liked were
www.velmorsnacks.com (simple but powerful, clean and clearly tells what the product is)
www.tirolinfare.com
Marla Voss's food
Tovi Crispy Chips

Current package AI file is on the following dropbox:

https://www.filevaultexample.com/sh/kq7wnd31xrtz/QWErtYuiOp_AsDfGhJkLzX?dl=0

Actual Product Image:
I've uploaded on my product page.

Our current package design needs to be completely changed into new design.
Updates

Hi I've uploaded both AI and PDF files of product actual image. Please put the actual product image. You don't have to put the exact same image (whether you put one roll image or whole group, I will leave up to the designer. Be creative!). Thanks.

Thank you for your participation in our project. Due to the production issue, we will need only one flavor (Cheese). We reviewed all of designs you have submitted and we felt there were many great designs. However, we felt none of design has reflected the feature of 21 grain. The main essential feature of this product is that it is made of 21 Multi Grains, and this point should be emphasized. This is the main feature that differentiates our product from others. This product is a healthy snack, and it can be a great meal replacement since it is made of 21 multi grains.

I will need only one design (I won't need Green Tea, Strawberry, Chocolate flavors). So I will need one design for one product (Oven Puffed Harvest Crunch Rounds). I showed all of your design drafts to my buyers. Buyers have commented that the none of the packages reflect or show that this product is made of 21 kind of multi grains. This is the very crucial important factor. I need a design that shows the product is made of multi grains so healthy snack. You can use my old existing design I've uploaded.

Target Market(s)

Mothers, LOHAS consumers, Millenials, Foodies

Industry/Entity Type

Food Production

Requirements
Must have
• 21 Multi Grain must be clearly and strongly emphasized on the package. This product is a special, healthy and unique snack because it is made of 21 kinds of Multi Grains!
Nice to have
• COLORFUL, CONSISTENCY
• I'VE UPLOADED THE OTHER COMPANIES' PACKAGES I LIKED
• http://www.bramwickpantry.com/products

```html
<!DOCTYPE html>
<html lang="en">
<head>
<meta charset="utf-8">
<title>Pelno – Oven Puffed Harvest Crunch Rounds pouch</title>
<link href="https://fonts.googleapis.com/css2?family=Kaushan+Script&family=Bebas+Neue&family=Oswald:wght@300;400&family=Nothing+You+Could+Do&display=swap" rel="stylesheet">
<style>
  :root{
    --page:#d9d8d8;
    --pouch-dark:#141313;
    --band:#1f1e1e;
    --band-edge:#2b2a2a;
    --ink:#d9cfc8;
    --ink-soft:#b9b0aa;
    --logo-red:#b3202a;
    --grain-brown:#7a4a25;
    --grain-gold:#c08a2e;
    --grain-red:#8e1f22;
    --grain-green:#3f6b22;
    --roll-light:#e2c088;
    --roll-dark:#a8773a;
  }
  *{margin:0;padding:0;box-sizing:border-box}
  html,body{width:1200px;height:1167px;overflow:hidden;background:var(--page)}
  .canvas{position:relative;width:1200px;height:1167px}

  .pouch{position:absolute;left:290px;top:45px;width:620px;height:1076px;
    border-radius:24px 24px 8px 8px;overflow:hidden;background:var(--pouch-dark)}
  .grain-backdrop{position:absolute;inset:0;
    background:
      radial-gradient(circle at 12% 12%, var(--grain-green) 0, transparent 22%),
      radial-gradient(circle at 90% 28%, var(--grain-gold) 0, transparent 20%),
      radial-gradient(circle at 90% 48%, var(--grain-red) 0, transparent 20%),
      radial-gradient(circle at 8% 45%, var(--grain-gold) 0, transparent 18%),
      radial-gradient(circle at 10% 80%, var(--grain-brown) 0, transparent 22%),
      radial-gradient(circle at 90% 85%, var(--grain-gold) 0, transparent 20%),
      linear-gradient(180deg,#2a1f18,#1a1512 60%,#2a2016)}
  .zip{position:absolute;left:0;right:0;top:124px;height:6px;
    background:linear-gradient(180deg,rgba(255,255,255,.12),rgba(0,0,0,.35))}

  .label-band{position:absolute;left:121px;top:0;width:365px;height:942px;
    background:var(--band);border-left:1px solid var(--band-edge);border-right:1px solid var(--band-edge)}

  .brand{position:absolute;top:48px;left:0;right:0;display:flex;justify-content:center;align-items:center;gap:10px}
  .brand-dot{width:22px;height:22px;border-radius:50%;background:var(--logo-red)}
  .brand-name{font-family:'Kaushan Script',cursive;font-size:34px;color:var(--ink);line-height:1}

  .product-name{position:absolute;top:150px;left:0;right:0;text-align:center;color:var(--ink);font-weight:400}
  .name-script{display:block;font-family:'Kaushan Script',cursive;line-height:1.05}
  .name-script.top{font-size:44px}
  .name-script.bottom{font-size:76px;margin-top:2px}
  .name-block{display:block;font-family:'Bebas Neue',sans-serif;line-height:.92;letter-spacing:1px}
  .name-block.grain{font-size:72px;margin-top:4px}
  .name-block.mid{font-size:54px}
  .name-block.big{font-size:100px}

  .tagline-vertical{position:absolute;left:22px;top:440px;transform-origin:left top;
    transform:translate(14px,0) rotate(90deg);white-space:nowrap;
    font-family:'Oswald',sans-serif;font-weight:300;font-size:14px;letter-spacing:2px;color:var(--ink-soft)}
  .tagline-vertical .accent{font-family:'Kaushan Script',cursive;font-size:18px;letter-spacing:0;margin:0 6px}

  .claim{position:absolute;left:40px;top:540px;width:300px;height:180px}
  .claim text{font-family:'Nothing You Could Do',cursive;fill:var(--ink);font-size:24px}

  .product-photo{position:absolute;left:85px;top:712px;width:210px;height:132px;border-radius:40% 30% 45% 35%;
    background:radial-gradient(circle at 45% 40%,var(--roll-light),var(--roll-dark) 75%,transparent 76%)}

  .size-info{position:absolute;left:22px;top:862px;font-family:'Oswald',sans-serif;font-weight:300;color:var(--ink-soft)}
  .size-row{display:flex;align-items:center;gap:14px;font-size:12px}
  .size-chip{width:18px;height:22px;border-radius:3px;background:var(--roll-light)}
  .net-weight{margin-top:14px;margin-left:20px;font-size:13px;letter-spacing:1px}

  .free-from{position:absolute;right:22px;top:898px;display:flex;gap:10px;
    font-family:'Nothing You Could Do',cursive;font-size:16px;color:var(--ink)}
  .free-from span{text-decoration:line-through}
</style>
</head>
<body>
<div class="canvas">
  <div class="pouch">
    <div class="grain-backdrop" role="img" aria-label="Overhead photo of wooden bowls filled with assorted grains, beans, seeds and pulses"></div>
    <div class="zip"></div>

    <div class="label-band">
      <div class="brand">
        <span class="brand-dot"></span>
        <span class="brand-name">Pelno</span>
      </div>

      <h1 class="product-name">
        <span class="name-script top">Oven Puffed</span>
        <span class="name-block grain">21 GRAIN</span>
        <span class="name-block mid">HARVEST</span>
        <span class="name-block big">CRUNCH</span>
        <span class="name-script bottom">Rounds</span>
      </h1>

      <p class="tagline-vertical">DISCOVER<span class="accent">21 grains</span>WORLD WITH AMAZING TASTE</p>

      <svg class="claim" viewBox="0 0 300 180" aria-label="amasing tast soft cream cheese">
        <defs>
          <path id="arc1" d="M50 60 Q150 5 280 75"/>
          <path id="arc2" d="M85 90 Q160 50 250 110"/>
          <path id="arc3" d="M115 125 Q150 108 195 130"/>
        </defs>
        <text><textPath href="#arc1">amasing tast</textPath></text>
        <text><textPath href="#arc2">soft cream</textPath></text>
        <text><textPath href="#arc3">cheese</textPath></text>
        <path d="M50 95 Q25 125 42 160" fill="none" stroke="var(--ink)" stroke-width="2"/>
        <path d="M33 152 L42 162 L50 151" fill="none" stroke="var(--ink)" stroke-width="2"/>
        <path d="M275 105 Q295 135 272 162" fill="none" stroke="var(--ink)" stroke-width="2"/>
        <path d="M266 150 L271 163 L283 158" fill="none" stroke="var(--ink)" stroke-width="2"/>
      </svg>

      <div class="product-photo" role="img" aria-label="Two baked grain rolls with soft cream cheese filling"></div>

      <div class="size-info">
        <div class="size-row"><span class="size-chip"></span><span>2.5 CM X 2 CM</span></div>
        <div class="net-weight">80 G / 2.82 OZ.FL</div>
      </div>

      <div class="free-from"><span>GMO</span><span>GLUTEN</span><span>FAT</span></div>
    </div>
  </div>
</div>
</body>
</html>
```